KESTRA Communications Business Card- Olde

Kestra Integrated Communications is Corporate communications agency with more than 20 years of experience. We become part of the manegement team of our clients in other to improve their outcomes and grow the possitioning of their brand.
We are in Puerto Rico, latin caribbean island
Name: Marisolde (Olde) Fuentes
787-555-0148
ofuentes@kestrakom.example

Target Market(s)

finance and pharmaceutical companies

Industry/Entity Type

Business

Contact Information for Business Card

modern, edgy colorful and playfull like our logo

Requirements
Must have
• company logo
• name
• tel
• email

```html
<!DOCTYPE html>
<html lang="en">
<head>
<meta charset="utf-8">
<title>Kestra Integrated Communications – Business Card</title>
<link rel="stylesheet" href="https://fonts.googleapis.com/css2?family=Crimson+Pro:wght@400;700&display=swap">
<style>
  :root {
    --brown: #3f2c00;
    --orange: #f05a22;
    --icon-orange: #e2603a;
    --paper: #ffffff;
    --backdrop: #ececec;
  }
  * { margin: 0; padding: 0; box-sizing: border-box; }
  html, body { width: 1200px; height: 1200px; overflow: hidden; }
  body {
    background: var(--backdrop);
    font-family: "Crimson Pro", "Palatino Linotype", Georgia, serif;
    position: relative;
  }
  .card {
    position: absolute;
    left: 163px;
    width: 900px;
    height: 540px;
    overflow: hidden;
  }
  .card--front { top: 50px; background: var(--paper); }
  .card--back { top: 619px; background: var(--orange); }

  .wordmark {
    font-family: "Crimson Pro", "Palatino Linotype", Georgia, serif;
    font-weight: 700;
    line-height: 1;
    white-space: nowrap;
  }
  .card--front .wordmark {
    position: absolute;
    left: 41px;
    top: 62px;
    font-size: 34px;
    color: var(--orange);
  }
  .card--back .wordmark {
    position: absolute;
    left: 0; right: 0;
    top: 232px;
    text-align: center;
    font-size: 68px;
    color: var(--brown);
  }

  .holder-name {
    position: absolute;
    right: 49px;
    top: 246px;
    font-size: 56px;
    font-weight: 700;
    color: var(--brown);
    letter-spacing: 0.5px;
    white-space: nowrap;
  }

  .footer-band {
    position: absolute;
    left: 0; top: 0;
    width: 900px; height: 540px;
  }

  .contact {
    position: absolute;
    top: 468px;
    display: flex;
    align-items: center;
    gap: 22px;
    color: var(--brown);
    font-size: 23px;
    white-space: nowrap;
  }
  .contact--phone { left: 43px; }
  .contact--email { left: 295px; font-size: 20px; gap: 20px; }
  .contact__icon { width: 35px; height: 35px; flex: none; }
</style>
</head>
<body>
  <section class="card card--front" aria-label="Business card front">
    <div class="wordmark">KESTRA Communications</div>

    <h1 class="holder-name">Marisolde Fuentes</h1>

    <svg class="footer-band" viewBox="0 0 900 540" aria-hidden="true">
      <polygon points="0,518 605,518 671,470 900,470 900,540 0,540" fill="var(--brown)"/>
    </svg>

    <div class="contact contact--phone">
      <svg class="contact__icon" viewBox="0 0 35 35" aria-hidden="true">
        <rect width="35" height="35" rx="4" fill="var(--icon-orange)"/>
        <path d="M12 7c-2 1-3 3-3 6 0 6 4 13 9 16 2 1 4 1 5 0l1-2-4-4-2 1c-2-2-4-6-4-9l2-1-1-6z" fill="#fff"/>
      </svg>
      <span>787-555-0148</span>
    </div>

    <div class="contact contact--email">
      <svg class="contact__icon" viewBox="0 0 35 35" aria-hidden="true">
        <rect width="35" height="35" rx="4" fill="var(--icon-orange)"/>
        <rect x="7" y="10" width="21" height="15" fill="none" stroke="#fff" stroke-width="2"/>
        <path d="M7 10l10.5 9L28 10M7 25l8-7M28 25l-8-7" fill="none" stroke="#fff" stroke-width="2"/>
      </svg>
      <span>ofuentes@kestrakom.example</span>
    </div>
  </section>

  <section class="card card--back" aria-label="Business card back">
    <div class="wordmark">KESTRA Communications</div>
  </section>
</body>
</html>
```